Velder Auto Repair - Flyer Design

My business is a automobile shop where we fix cars. Such things that we do but not limited to is brakes, Engine/Transmission change, Electrical work, emission test, oil change and automobile diagnostic. I am looking for a flyer that will catch peoples attention, I will be giving flyers to people, putting them in car windows and mailboxes. I am looking for a flier that will help to attract more customers to my business. I also want the flyer to say "Bring in your estimate from our competitors with this flyer and we will beat it by 10%" (does not have to be in those exact words). I also want the flyer to have my business address phone and operating hours. I have attached a business card and my business ad which I have placed in the newspaper before. I hope it helps with your design.
Industry/Entity Type
Car Repair
Look and feel

```html
<!DOCTYPE html>
<html lang="en">
<head>
<meta charset="UTF-8">
<title>Velder Auto Repair – Flyer</title>
<link rel="stylesheet" href="https://fonts.googleapis.com/css2?family=Exo+2:ital,wght@1,600;1,700&family=Montserrat:wght@600&family=Roboto+Condensed:ital,wght@0,700;1,400&display=swap">
<style>
  :root {
    --red: #d71f27;
    --red-dark: #b3151c;
    --cream: #f1efe8;
    --navy: #1c2340;
    --white: #ffffff;
  }
  * { margin: 0; padding: 0; box-sizing: border-box; }
  html, body { width: 903px; height: 1200px; overflow: hidden; background: var(--cream); }
  .flyer {
    position: relative; width: 903px; height: 1200px;
    background: var(--cream); overflow: hidden;
  }
  .top-band {
    position: absolute; left: 0; top: 0; width: 100%; height: 360px;
    background: linear-gradient(180deg, var(--red) 0%, var(--red-dark) 100%);
  }
  .hours {
    position: absolute; left: 42px; top: 30px;
    font: italic 400 19px/1 "Roboto Condensed", sans-serif; color: var(--white);
  }
  .brand-name {
    position: absolute; left: 42px; top: 62px;
    font: 600 62px/1 "Montserrat", sans-serif; color: var(--white); letter-spacing: 0.5px;
  }
  .hero-photo {
    position: absolute; left: 42px; top: 156px; width: 819px; height: 422px;
    border: 3px solid var(--white);
    background: radial-gradient(ellipse at 50% 62%, #c8252b 0%, #8e3a3c 22%, #b9bcc2 48%, #dcdde0 100%);
  }
  .detail-photos {
    position: absolute; left: 42px; top: 592px; width: 819px; height: 176px;
    display: flex; justify-content: space-between;
  }
  .detail-photo { width: 264px; height: 176px; border: 3px solid var(--red); }
  .detail-photo.engine { background: linear-gradient(135deg, #2b2d33 0%, #5a5d66 60%, #a9acb3 100%); }
  .detail-photo.service { background: linear-gradient(135deg, #dfe2e7 0%, #8d98b0 50%, #2d3a66 100%); }
  .detail-photo.oil { background: linear-gradient(135deg, #4a4f5a 0%, #9aa0aa 55%, #c8a24a 100%); }
  .tagline {
    position: absolute; left: 42px; top: 788px; width: 819px; text-align: center;
    font: italic 700 33px/1 "Exo 2", sans-serif; color: var(--red); letter-spacing: 1px;
  }
  .services {
    position: absolute; left: 42px; top: 874px;
    display: grid; grid-template-columns: 247px 240px; row-gap: 12px;
    list-style: none;
    font: italic 600 27px/1 "Exo 2", sans-serif; color: var(--navy);
  }
  .services li::before { content: "» "; }
  .offer-badge { position: absolute; left: 662px; top: 846px; width: 200px; height: 250px; }
  .offer-text {
    position: absolute; left: 692px; top: 903px; width: 140px; text-align: center;
    font: 700 13px/1.1 "Roboto Condensed", sans-serif; color: var(--navy);
    text-transform: uppercase; white-space: nowrap;
  }
  .address {
    position: absolute; left: 0; top: 1060px; width: 903px; text-align: center;
    font: italic 700 23px/1 "Exo 2", sans-serif; color: var(--navy); letter-spacing: 0.5px;
  }
  .footer-rule { position: absolute; left: 0; top: 1092px; width: 100%; height: 5px; background: var(--red); }
  .footer {
    position: absolute; left: 0; top: 1101px; width: 100%; height: 99px; background: var(--navy);
    color: var(--white); text-align: center;
  }
  .call-line {
    margin-top: 16px; display: flex; justify-content: center; align-items: center; gap: 18px;
    font: italic 700 38px/1 "Exo 2", sans-serif;
  }
  .call-line svg { width: 34px; height: 34px; }
  .email { margin-top: 10px; font: italic 600 20px/1 "Exo 2", sans-serif; letter-spacing: 0.5px; }
</style>
</head>
<body>
<main class="flyer">
  <div class="top-band"></div>
  <p class="hours">HOURS: Mon - Fri: 8am-5 pm &nbsp;•&nbsp; Sat: 8am-4pm &nbsp;•&nbsp; Sun: Closed</p>
  <h1 class="brand-name">Velder Auto Repair</h1>

  <div class="hero-photo" role="img" aria-label="Red sports car raised on a lift inside a repair garage"></div>

  <div class="detail-photos">
    <div class="detail-photo engine" role="img" aria-label="Mechanic working in an engine bay"></div>
    <div class="detail-photo service" role="img" aria-label="Mechanic talking with a customer beside a car"></div>
    <div class="detail-photo oil" role="img" aria-label="Fresh oil being poured into an engine"></div>
  </div>

  <h2 class="tagline">Auto Mehanic Specialist Domestic &amp; Foreign</h2>

  <ul class="services">
    <li>Exhaust</li><li>Clutches</li>
    <li>Brakes</li><li>Tyres</li>
    <li>Suspensions</li><li>Services</li>
    <li>Engine</li><li>Transmission</li>
  </ul>

  <svg class="offer-badge" viewBox="0 0 200 250" aria-hidden="true">
    <polygon fill="#d71f27" points="66,168 134,168 100,250"/>
    <polygon fill="#d71f27" points="100,2 113.4,15 130.3,6.8 139,23.4 157.6,20.7 160.8,39.2 179.3,42.4 176.6,61 193.2,69.7 184.9,86.6 198,100 184.9,113.4 193.2,130.3 176.6,139 179.3,157.6 160.8,160.8 157.6,179.3 139,176.6 130.3,193.2 113.4,185 100,198 86.6,185 69.7,193.2 61,176.6 42.4,179.3 39.2,160.8 20.7,157.6 23.4,139 6.8,130.3 15.1,113.4 2,100 15.1,86.6 6.8,69.7 23.4,61 20.7,42.4 39.2,39.2 42.4,20.7 61,23.4 69.7,6.8 86.6,15"/>
    <circle cx="100" cy="100" r="76" fill="#ffffff" stroke="#e4e4ea" stroke-width="3"/>
  </svg>
  <p class="offer-text">Bring in<br>your estimate<br>from our competitors<br>with this flyer<br>and we will beat<br>it by 10%</p>

  <p class="address">4120 W. Harbor Ave. Chicago Il. 60699</p>

  <div class="footer-rule"></div>
  <footer class="footer">
    <div class="call-line">
      <span>Call Now</span>
      <svg viewBox="0 0 24 24" aria-hidden="true">
        <path fill="#ffffff" d="M6.6 10.8c1.4 2.8 3.8 5.1 6.6 6.6l2.2-2.2c.3-.3.7-.4 1-.2 1.1.4 2.3.6 3.6.6.6 0 1 .4 1 1V20c0 .6-.4 1-1 1C10.6 21 3 13.4 3 4c0-.6.4-1 1-1h3.5c.6 0 1 .4 1 1 0 1.3.2 2.5.6 3.6.1.3 0 .7-.2 1L6.6 10.8z"/>
        <path fill="none" stroke="#ffffff" stroke-width="1.6" stroke-linecap="round" d="M14.5 3.5a6 6 0 0 1 6 6M14.5 7a2.6 2.6 0 0 1 2.6 2.6"/>
      </svg>
      <span>773-555-0148</span>
    </div>
    <p class="email">velderautorepair@mailbox.com</p>
  </footer>
</main>
</body>
</html>
```